Multi Academy Trust needs to shout about our vision by turning our words into something that can ...

Our vision is something we want to shout about and share through multiple media avenues to a range of stakeholders including parents, staff, pupils, other school trusts, Board of Scholastic Affairs and suppliers. We want an eye-catching design that stands out from the crowd but incorporates our current brand (and logo)

```html
<!DOCTYPE html>
<html lang="en">
<head>
<meta charset="utf-8">
<title>Our Vision – Northbridge Learning Trust</title>
<link rel="stylesheet" href="https://fonts.googleapis.com/css2?family=Raleway:wght@400;500;600;700;800;900&display=swap">
<style>
:root{
  --blue-deep:#0959b2;
  --blue-mid:#0a7cc6;
  --blue-bright:#1490d8;
  --blue-soft:#7cc4ee;
  --grey-dark:#58585a;
  --text:#2f2f31;
  --white:#ffffff;
  --page:#ffffff;
}
*{margin:0;padding:0;box-sizing:border-box}
html,body{width:966px;height:1200px;overflow:hidden;background:var(--page)}
body{font-family:"Raleway",sans-serif;color:var(--text)}
.poster{position:relative;width:966px;height:1200px;background:var(--white)}

/* brand */
.brand{position:absolute;left:44px;top:46px;display:flex;align-items:center;gap:18px}
.brand-dot{width:96px;height:96px;border-radius:50%;background:var(--blue-bright)}
.brand-name{font-family:"Raleway",sans-serif;font-weight:500;font-size:27px;line-height:30px;color:var(--grey-dark)}

/* left panel */
.vision-panel{position:absolute;left:0;top:203px;width:482px;height:997px;
  background:linear-gradient(180deg,var(--blue-mid) 0%,#0b86cc 40%,#0a73c2 100%);
  border-top-right-radius:46px;overflow:hidden;color:var(--white)}
.vision-head{height:91px;background:var(--blue-deep);display:flex;align-items:center;padding-left:28px;gap:26px}
.vision-head h2{font-weight:900;font-size:37px;line-height:38px;letter-spacing:.2px}
.vision-head p{font-weight:800;font-size:21px;margin-top:1px}
.purpose{position:relative;height:312px}
.purpose-title{position:absolute;left:40px;top:28px;font-weight:400;font-size:47px;line-height:50px;letter-spacing:-.5px;white-space:nowrap}
.purpose-title strong{font-weight:900;display:block;font-size:51px;line-height:52px}
.purpose-text{position:absolute;left:42px;top:144px;width:415px;font-size:21px;line-height:29px;font-weight:500}
.purpose-text strong{font-weight:800}
.ensure-head{height:82px;background:var(--blue-deep);display:flex;align-items:center;padding-left:28px;gap:32px}
.ensure-head h3{font-weight:900;font-size:24px;line-height:27px}
.values-intro{position:absolute;left:42px;top:498px;font-size:27px;font-weight:600}
.value{position:absolute;left:40px;display:flex;align-items:center;width:442px}
.value-icon{width:84px;height:84px;border:2px solid var(--blue-soft);border-radius:50%;display:flex;align-items:center;justify-content:center;flex:none}
.value-text{margin-left:25px;font-size:22.5px;line-height:30px;font-weight:500;white-space:nowrap}
.value-rule{position:absolute;left:149px;right:0;height:1px;background:rgba(255,255,255,.45)}

/* right column */
.look-title{position:absolute;left:513px;top:34px;font-weight:900;font-size:42px;line-height:44px;color:var(--grey-dark);letter-spacing:-.3px}
.look-title span{color:var(--blue-bright)}
.pillar{position:absolute;left:513px;width:430px}
.pillar-head{position:relative;height:88px}
.pillar-pill{position:absolute;left:44px;top:21px;width:265px;height:46px;border-radius:0 23px 23px 0;
  display:flex;align-items:center;padding-left:58px;color:var(--white);font-weight:900;font-size:29px}
.pillar-badge{position:absolute;left:0;top:0;width:88px;height:88px;border-radius:50%;background:var(--white);
  border:3px solid currentColor;display:flex;align-items:center;justify-content:center}
.pillar--blue{color:var(--blue-bright)}
.pillar--blue .pillar-pill{background:var(--blue-bright)}
.pillar--grey{color:var(--grey-dark)}
.pillar--grey .pillar-pill{background:var(--grey-dark)}
.pillar-lead{margin:20px 0 6px 52px;font-size:15.5px;font-weight:500;color:var(--text)}
.checks{list-style:none}
.checks li{display:flex;font-size:15.5px;line-height:20px;font-weight:500;color:var(--text);margin-bottom:6px;white-space:nowrap}
.checks svg{flex:none;margin:2px 16px 0 20px}
</style>
</head>
<body>
<main class="poster">

  <div class="brand">
    <span class="brand-dot"></span>
    <div class="brand-name">Northbridge<br>Learning<br>Trust</div>
  </div>

  <section class="vision-panel">
    <header class="vision-head">
      <svg width="72" height="64" viewBox="0 0 72 64" fill="none" stroke="#8fd0f3" stroke-width="5">
        <circle cx="30" cy="34" r="26"/><circle cx="30" cy="34" r="16"/><circle cx="30" cy="34" r="5" fill="#8fd0f3"/>
        <path d="M30 34 L60 8" stroke-width="4"/><path d="M54 4 L66 2 L64 14" stroke-width="4"/>
      </svg>
      <div><h2>OUR VISION</h2><p>DRAFT3@ DECEMBER 2019</p></div>
    </header>

    <div class="purpose">
      <h1 class="purpose-title">WE HAVE ONE<strong>CORE PURPOSE:</strong></h1>
      <p class="purpose-text">To have <strong>THE BIGGEST POSITIVE<br>IMPACT</strong> in the varied communities we<br>serve through ensuring top drawer<br>educationfor our learners.<br><strong>#BrighterFutures</strong></p>
    </div>

    <header class="ensure-head">
      <svg width="50" height="44" viewBox="0 0 50 44" fill="none" stroke="#fff" stroke-width="3" stroke-linejoin="round">
        <path d="M3 14 L14 6 L26 10 L36 6 L47 14"/>
        <path d="M8 22 L22 38 Q26 41 29 37 L40 26 L47 14"/>
        <path d="M26 10 L18 18 Q22 22 28 17 L36 24"/>
        <path d="M14 28 L20 34 M19 24 L25 30"/>
      </svg>
      <h3>HOW DO WE ENSURE<br>THIS ACROSS OUR TRUST?</h3>
    </header>

    <p class="values-intro">In all we do we are:</p>

    <div class="value" style="top:556px">
      <span class="value-icon"><svg width="44" height="40" viewBox="0 0 44 40" fill="none" stroke="#8fd0f3" stroke-width="2.5" stroke-linejoin="round"><path d="M2 12 L22 4 L42 12 L22 20 Z"/><path d="M10 16 V28 Q22 36 34 28 V16"/><path d="M38 14 V26"/></svg></span>
      <p class="value-text">Ethical to the core,<br>ensuring that education is<br>always front and centre</p>
    </div>
    <span class="value-rule" style="top:654px"></span>

    <div class="value" style="top:668px">
      <span class="value-icon"><svg width="44" height="44" viewBox="0 0 44 44" fill="none" stroke="#8fd0f3" stroke-width="2.5"><circle cx="20" cy="20" r="11"/><circle cx="20" cy="20" r="16" stroke-dasharray="6 5"/><path d="M28 28 L38 38" stroke-width="4"/></svg></span>
      <p class="value-text">Futures focused system<br>leaders – never simply<br>followers</p>
    </div>
    <span class="value-rule" style="top:769px"></span>

    <div class="value" style="top:774px">
      <span class="value-icon"><svg width="46" height="44" viewBox="0 0 46 44" fill="none" stroke="#8fd0f3" stroke-width="2.2"><circle cx="23" cy="8" r="4"/><path d="M16 20 Q23 12 30 20 Z"/><circle cx="9" cy="28" r="4"/><path d="M2 40 Q9 32 16 40 Z"/><circle cx="37" cy="28" r="4"/><path d="M30 40 Q37 32 44 40 Z"/><path d="M8 18 Q10 8 16 6 M38 18 Q36 8 30 6 M18 34 H28"/></svg></span>
      <p class="value-text">Collaborative in every<br>endeavour</p>
    </div>
    <span class="value-rule" style="top:869px"></span>

    <div class="value" style="top:870px">
      <span class="value-icon"><svg width="44" height="46" viewBox="0 0 44 46" fill="none" stroke="#8fd0f3" stroke-width="2.5"><path d="M22 10 Q32 10 32 20 Q32 26 27 30 V34 H17 V30 Q12 26 12 20 Q12 10 22 10 Z"/><path d="M17 38 H27 M18 42 H26 M22 2 V5 M6 8 L9 11 M38 8 L35 11 M2 20 H5 M39 20 H42"/></svg></span>
      <p class="value-text">Resolutely learner centred.</p>
    </div>
  </section>

  <h2 class="look-title"><span>WHAT DOES THIS</span><br>LOOK LIKE ACROSS<br>OUR TRUST?</h2>

  <section class="pillar pillar--blue" style="top:178px">
    <div class="pillar-head">
      <div class="pillar-pill">EDUCATION</div>
      <span class="pillar-badge"><svg width="52" height="40" viewBox="0 0 52 40" fill="currentColor"><path d="M2 12 L26 3 L50 12 L26 21 Z"/><path d="M11 17 V28 Q26 36 41 28 V17 L26 23 Z"/><path d="M6 14 V30" stroke="currentColor" stroke-width="2.5"/><circle cx="6" cy="32" r="3"/></svg></span>
    </div>
    <p class="pillar-lead">We are:</p>
    <ul class="checks">
      <li><svg width="16" height="16" viewBox="0 0 16 16" fill="none" stroke="#1490d8" stroke-width="1.8"><path d="M14 7.5 A6.5 6.5 0 1 1 10 1.8"/><path d="M4.5 7.5 L7.5 10.5 L15 2.5"/></svg><span>Ruthlessly ambitious for all who learn and work<br>with us</span></li>
      <li><svg width="16" height="16" viewBox="0 0 16 16" fill="none" stroke="#1490d8" stroke-width="1.8"><path d="M14 7.5 A6.5 6.5 0 1 1 10 1.8"/><path d="M4.5 7.5 L7.5 10.5 L15 2.5"/></svg><span>Unwaveringly inclusive – determined on<br>eradicating barriers to educationalsuccess</span></li>
      <li><svg width="16" height="16" viewBox="0 0 16 16" fill="none" stroke="#1490d8" stroke-width="1.8"><path d="M14 7.5 A6.5 6.5 0 1 1 10 1.8"/><path d="M4.5 7.5 L7.5 10.5 L15 2.5"/></svg><span>Committed to excellentteaching</span></li>
      <li><svg width="16" height="16" viewBox="0 0 16 16" fill="none" stroke="#1490d8" stroke-width="1.8"><path d="M14 7.5 A6.5 6.5 0 1 1 10 1.8"/><path d="M4.5 7.5 L7.5 10.5 L15 2.5"/></svg><span>Determined upon academic excellence for all in<br>our communities</span></li>
      <li><svg width="16" height="16" viewBox="0 0 16 16" fill="none" stroke="#1490d8" stroke-width="1.8"><path d="M14 7.5 A6.5 6.5 0 1 1 10 1.8"/><path d="M4.5 7.5 L7.5 10.5 L15 2.5"/></svg><span>Compassionate, ethical and caring advocates<br>for all in our communities</span></li>
      <li><svg width="16" height="16" viewBox="0 0 16 16" fill="none" stroke="#1490d8" stroke-width="1.8"><path d="M14 7.5 A6.5 6.5 0 1 1 10 1.8"/><path d="M4.5 7.5 L7.5 10.5 L15 2.5"/></svg><span>Outwardly facing and globally conscious</span></li>
    </ul>
  </section>

  <section class="pillar pillar--grey" style="top:562px">
    <div class="pillar-head">
      <div class="pillar-pill">OPERATIONS</div>
      <span class="pillar-badge"><svg width="62" height="40" viewBox="0 0 62 40" fill="currentColor"><circle cx="31" cy="20" r="12"/><circle cx="31" cy="20" r="5" fill="#fff"/><g stroke="currentColor" stroke-width="5"><path d="M31 4 V36 M15 20 H47 M20 9 L42 31 M42 9 L20 31"/></g><circle cx="31" cy="20" r="5" fill="#fff"/><circle cx="10" cy="20" r="7"/><circle cx="10" cy="20" r="3" fill="#fff"/><circle cx="52" cy="20" r="7"/><circle cx="52" cy="20" r="3" fill="#fff"/></svg></span>
    </div>
    <p class="pillar-lead">We are:</p>
    <ul class="checks">
      <li><svg width="16" height="16" viewBox="0 0 16 16" fill="none" stroke="#1490d8" stroke-width="1.8"><path d="M14 7.5 A6.5 6.5 0 1 1 10 1.8"/><path d="M4.5 7.5 L7.5 10.5 L15 2.5"/></svg><span>Committed to the very best people development<br>and empowerment</span></li>
      <li><svg width="16" height="16" viewBox="0 0 16 16" fill="none" stroke="#1490d8" stroke-width="1.8"><path d="M14 7.5 A6.5 6.5 0 1 1 10 1.8"/><path d="M4.5 7.5 L7.5 10.5 L15 2.5"/></svg><span>Determined to shout loudly and share proudly our<br>successes</span></li>
      <li><svg width="16" height="16" viewBox="0 0 16 16" fill="none" stroke="#1490d8" stroke-width="1.8"><path d="M14 7.5 A6.5 6.5 0 1 1 10 1.8"/><path d="M4.5 7.5 L7.5 10.5 L15 2.5"/></svg><span>The best professional and technical experts<br>(supporting education) in the sector</span></li>
      <li><svg width="16" height="16" viewBox="0 0 16 16" fill="none" stroke="#1490d8" stroke-width="1.8"><path d="M14 7.5 A6.5 6.5 0 1 1 10 1.8"/><path d="M4.5 7.5 L7.5 10.5 L15 2.5"/></svg><span>Committed to the very best understanding and<br>management of risk</span></li>
    </ul>
  </section>

  <section class="pillar pillar--blue" style="top:884px">
    <div class="pillar-head">
      <div class="pillar-pill">FINANCIAL</div>
      <span class="pillar-badge"><svg width="50" height="44" viewBox="0 0 50 44" fill="currentColor"><circle cx="28" cy="12" r="10"/><text x="28" y="17" font-family="Raleway,sans-serif" font-size="14" font-weight="700" fill="#fff" text-anchor="middle">$</text><rect x="2" y="26" width="8" height="14"/><path d="M12 28 H28 Q32 28 32 31 H22 V33 H36 L46 26 Q49 28 46 31 L36 40 H12 Z"/></svg></span>
    </div>
    <p class="pillar-lead">We are:</p>
    <ul class="checks">
      <li><svg width="16" height="16" viewBox="0 0 16 16" fill="none" stroke="#1490d8" stroke-width="1.8"><path d="M14 7.5 A6.5 6.5 0 1 1 10 1.8"/><path d="M4.5 7.5 L7.5 10.5 L15 2.5"/></svg><span>Providing the best possible public service for the<br>best possible value</span></li>
      <li><svg width="16" height="16" viewBox="0 0 16 16" fill="none" stroke="#1490d8" stroke-width="1.8"><path d="M14 7.5 A6.5 6.5 0 1 1 10 1.8"/><path d="M4.5 7.5 L7.5 10.5 L15 2.5"/></svg><span>Determined to supplement our public income with<br>shrewd income generation</span></li>
      <li><svg width="16" height="16" viewBox="0 0 16 16" fill="none" stroke="#1490d8" stroke-width="1.8"><path d="M14 7.5 A6.5 6.5 0 1 1 10 1.8"/><path d="M4.5 7.5 L7.5 10.5 L15 2.5"/></svg><span>Building financially sustainable models of<br>educational improvement in our communities</span></li>
      <li><svg width="16" height="16" viewBox="0 0 16 16" fill="none" stroke="#1490d8" stroke-width="1.8"><path d="M14 7.5 A6.5 6.5 0 1 1 10 1.8"/><path d="M4.5 7.5 L7.5 10.5 L15 2.5"/></svg><span>Demonstrably efficient in all we do</span></li>
    </ul>
  </section>

</main>
</body>
</html>
```